Wooden Floor Website

I'd like a Modern and crisp site with emphasis on the site being easy to navigate through - services that we offer, gallery of previous work, history, who we are, contact, etc
https://vaultqx8261937-my.filedeckly.com/:b:/g/personal/tobias_pellwickhaus_co_uk/QWM7R2_kpLsTbNVafrxHoZWCKdYeP8u3G6vRPMsLmoXBtc

Coded - Design and coding required

5+ page

• Word Press Site

```html
<!DOCTYPE html>
<html lang="en">
<head>
<meta charset="utf-8">
<title>Pellwickhaus – Bespoke Wood Floors</title>
<link href="https://fonts.googleapis.com/css2?family=Lato:wght@300;400;700;900&display=swap" rel="stylesheet">
<style>
:root{
  --gold:#a8905d;
  --gold-dark:#8f784a;
  --ink:#222;
  --text:#555;
  --muted:#9a9a9a;
  --line:#d8d8d8;
  --white:#fff;
  --dark:#262220;
  --footer-base:#2b1e15;
}
*{box-sizing:border-box;margin:0;padding:0}
html,body{width:1200px;height:3280px;overflow:hidden}
body{position:relative;font-family:'Lato',Arial,sans-serif;color:var(--text);background:var(--white)}
.abs{position:absolute}
.img{position:absolute}

/* top bar */
.topbar{left:0;top:0;width:1200px;height:36px;background:var(--gold);color:var(--white);font-size:13px}
.topbar .contact{left:170px;top:10px;display:flex;gap:22px}
.topbar .contact span{display:flex;align-items:center;gap:6px}
.topbar .account{right:170px;top:10px;display:flex;gap:16px;align-items:center}
.dot{width:10px;height:10px;border-radius:50%;background:var(--white);display:inline-block}

/* header */
.header{left:0;top:36px;width:1200px;height:92px;background:var(--white)}
.brand{left:170px;top:16px;display:flex;flex-direction:column;align-items:center;gap:8px}
.brand .mark{width:34px;height:34px;border:2px solid var(--ink)}
.brand .name{font-size:12px;font-weight:700;letter-spacing:1px;color:var(--ink)}
.nav{left:405px;top:38px;display:flex;gap:26px;font-size:14px;color:var(--ink)}
.nav .active{color:var(--gold)}
.search{left:760px;top:32px;width:265px;height:28px;border:1px solid var(--line)}
.search svg{position:absolute;right:8px;top:7px}

/* hero */
.hero{left:0;top:128px;width:1200px;height:532px;background:linear-gradient(180deg,#c9c3b5 0%,#d9d3c6 45%,#b7aa98 100%)}
.hero-title{left:240px;top:186px;width:722px;height:50px;background:#111;color:var(--white);font-size:34px;font-weight:400;letter-spacing:1px;text-align:center;line-height:50px}
.btn{border-radius:20px;text-align:center;font-size:13px}
.btn-light{left:492px;top:260px;width:218px;height:39px;line-height:39px;background:var(--white);color:var(--ink)}
.arrow{top:246px;width:24px;height:40px;background:rgba(0,0,0,.35)}
.features{top:400px}
.feature{display:flex;gap:12px;width:270px}
.feature .thumb{width:76px;height:76px;flex:none}
.feature h4{font-size:12px;font-weight:700;text-decoration:underline;text-transform:uppercase;color:var(--white);margin-top:4px}
.feature p{font-size:12px;color:var(--white);line-height:1.35;margin-top:4px}

/* intro */
.intro-title{left:0;top:724px;width:1200px;text-align:center;font-size:34px;font-weight:400;color:var(--ink)}
.intro-copy{left:185px;top:796px;width:830px;text-align:center;font-size:14px;line-height:1.65;color:#444}
.btn-gold{background:var(--gold);color:var(--white)}
.intro-btn{left:536px;top:886px;width:128px;height:32px;line-height:32px}
.intro-note{left:300px;top:958px;width:600px;text-align:center;font-size:12.5px;line-height:1.7;color:#444}
.divider{left:0;top:1071px;width:1200px;height:1px;background:#eee}

/* section headings */
.sec-head{left:0;width:1200px;display:flex;justify-content:center;align-items:center;gap:22px;font-size:36px;font-weight:400;color:var(--ink)}
.sec-head .rule{width:60px;height:2px;background:#999}
.sec-head em{font-style:normal;font-weight:700;color:var(--gold)}

/* collection */
.card{top:1238px;width:272px}
.card .photo{width:272px;height:202px;position:relative}
.card h3{margin-top:22px;font-size:19px;font-weight:700;color:var(--ink)}
.card p{margin-top:8px;font-size:12.5px;line-height:1.45;color:#444}
.card .more{margin-top:14px;font-size:11px;font-weight:700;color:var(--ink)}

/* process */
.process{left:0;top:1626px;width:1200px;height:429px;background:linear-gradient(100deg,#1c1917 0%,#2c2723 45%,#3b342d 100%)}
.process h2{left:170px;top:96px;font-size:36px;font-weight:400;color:var(--gold);letter-spacing:1px}
.process .lead{left:170px;top:146px;width:330px;font-size:14px;font-weight:700;color:var(--white);line-height:1.35}
.process .body{left:170px;top:216px;width:355px;font-size:12.5px;color:var(--white);line-height:1.6}
.step{width:200px;text-align:center;color:var(--white);font-size:12px;font-weight:700;text-transform:uppercase}
.step svg{display:block;margin:0 auto 12px}
.finish{left:831px;top:214px;width:194px;height:120px;background:var(--white);text-align:center;padding:12px 10px}
.finish h4{font-size:12px;font-weight:900;color:var(--ink)}
.finish p{font-size:11px;color:#333;line-height:1.4;margin-top:6px}

/* projects */
.project-photo{width:418px;height:257px}
.project h3{font-size:15px;font-weight:400;color:var(--ink)}
.tag{display:inline-block;margin-top:6px;padding:3px 8px;background:var(--gold);color:var(--white);font-size:10.5px}
.project p{margin-top:14px;font-size:12.5px;line-height:1.55;color:#a3a3a3}
.project .link{margin-top:14px;font-size:12px;color:var(--ink)}
.proj-btn{left:511px;top:2793px;width:176px;height:41px;line-height:41px;font-size:13px}

/* footer */
.footer{left:0;top:2883px;width:1200px;height:355px;background:linear-gradient(180deg,#3a2a1e 0%,#2a1d14 60%,#1e150f 100%)}
.footer .brand .mark{border-color:var(--white)}
.footer .brand .name{color:var(--white)}
.footer-about{left:170px;top:140px;width:250px;font-size:12.5px;color:#e8e2da;line-height:1.5}
.footer-about .more{text-decoration:underline;display:block}
.fcol h4{font-size:15px;font-weight:700;color:var(--white);margin-bottom:14px}
.fcol li{list-style:none;font-size:12.5px;color:#e8e2da;margin-bottom:8px;display:flex;align-items:center;gap:8px}
.tri{width:0;height:0;border-left:5px solid var(--white);border-top:4px solid transparent;border-bottom:4px solid transparent}
.copyright{left:0;top:3238px;width:1200px;height:42px;background:#1a1816;color:#9a948c;font-size:11px;text-align:center;line-height:42px}
</style>
</head>
<body>

<!-- top bar -->
<div class="abs topbar">
  <div class="abs contact">
    <span><svg width="11" height="11" viewBox="0 0 12 12"><path d="M2 1h3l1 3-2 1a7 7 0 0 0 3 3l1-2 3 1v3c-6 1-10-3-9-9z" fill="#fff"/></svg>+44 (0)20 7946 0321</span>
    <span><svg width="12" height="9" viewBox="0 0 12 9"><rect x=".5" y=".5" width="11" height="8" fill="none" stroke="#fff"/><path d="M.5.5 6 5l5.5-4.5" fill="none" stroke="#fff"/></svg>enquiries@pellwickhaus.co.uk</span>
  </div>
  <div class="abs account">
    <span>Sign Up / Login</span>
    <span>Cart <svg width="12" height="11" viewBox="0 0 12 11"><path d="M0 1h2l2 6h6l1-4H3" fill="none" stroke="#fff"/><circle cx="5" cy="9.5" r="1" fill="#fff"/><circle cx="9" cy="9.5" r="1" fill="#fff"/></svg></span>
    <span style="display:flex;gap:6px"><i class="dot"></i><i class="dot"></i><i class="dot"></i></span>
  </div>
</div>

<!-- header -->
<header class="abs header">
  <div class="abs brand"><span class="mark"></span><span class="name">PELLWICKHAUS</span></div>
  <nav class="abs nav">
    <span class="active">Home</span><span>About ▾</span><span>Products ▾</span><span>Work Gallery</span><span>Contact</span>
  </nav>
  <div class="abs search"><svg width="13" height="13" viewBox="0 0 13 13"><circle cx="5.5" cy="5.5" r="4.5" fill="none" stroke="#666" stroke-width="1.5"/><path d="M9 9l3.5 3.5" stroke="#666" stroke-width="1.5"/></svg></div>
</header>

<!-- hero -->
<section class="abs hero" role="img" aria-label="Bright living room with pale wide oak plank flooring, armchairs, plants and a round table"></section>
<div class="abs hero-title">CREATING EXCEPTIONAL BESPOKE FLOORS</div>
<div class="abs btn btn-light" style="top:388px">View Our All Products</div>
<div class="abs arrow" style="left:0;top:374px"><svg width="24" height="40"><path d="M15 13l-6 7 6 7" fill="none" stroke="#fff" stroke-width="2"/></svg></div>
<div class="abs arrow" style="right:0;top:374px"><svg width="24" height="40"><path d="M9 13l6 7-6 7" fill="none" stroke="#fff" stroke-width="2"/></svg></div>
<div class="abs features" style="left:170px;top:528px">
  <div class="feature"><div class="thumb" role="img" aria-label="Oak wood sample" style="background:linear-gradient(135deg,#b88c55,#9a7040)"></div><div><h4>Designs &amp; Dimensions</h4><p>Lorem ipsum dolor sit amet, consectetur adipiscing elit</p></div></div>
</div>
<div class="abs features" style="left:465px;top:528px">
  <div class="feature"><div class="thumb" role="img" aria-label="Wood grading sample" style="background:linear-gradient(135deg,#c49a63,#a07848)"></div><div><h4>Grading</h4><p>Lorem ipsum dolor sit amet, consectetur adipiscing elit</p></div></div>
</div>
<div class="abs features" style="left:757px;top:528px">
  <div class="feature"><div class="thumb" role="img" aria-label="Dark treated wood sample" style="background:linear-gradient(135deg,#5a4030,#3b2a1f)"></div><div><h4>Textures &amp; Treatments</h4><p>Lorem ipsum dolor sit amet, consectetur adipiscing elit</p></div></div>
</div>

<!-- intro -->
<h1 class="abs intro-title">Creating your exceptional wood floora</h1>
<p class="abs intro-copy">With endless options available, you can choose the design, dimensions, grade, texture, colour and finish all produced to order in the UK. Combining the finest sustainable FSC European Oak with the latest state of the art machinery, finishing products and highly skilled colour technicians, we will together create your bespoke wood floor.</p>
<div class="abs btn btn-gold intro-btn">Read More</div>
<p class="abs intro-note">PELLWICKHAUS offer a range of fully bespoke finished wood flooring as planks, herringbone blocks and chevrons; styles to suit any interior design.</p>
<div class="abs divider"></div>

<!-- collection -->
<h2 class="abs sec-head" style="top:1144px"><span class="rule"></span><span>Our <em>Collection</em></span><span class="rule"></span></h2>
<article class="abs card" style="left:170px">
  <div class="photo" role="img" aria-label="Oak plank flooring sample" style="background:linear-gradient(90deg,#c08a4e,#d3a06a 50%,#b98349)"></div>
  <h3>PLANK COLLECTION</h3>
  <p>PELLWICKHAUS offer you the option of thickness,width and grade in your chosen finish.</p>
  <div class="more">Read more</div>
</article>
<article class="abs card" style="left:462px">
  <div class="photo" role="img" aria-label="Dark herringbone oak flooring sample" style="background:linear-gradient(135deg,#6a5140,#4e3a2c)"></div>
  <h3>HERRINGBONE COLLECTION</h3>
  <p>Our classic herringbone blocks are also available in our bespoke range of 28 finishes to complement our Plank collection.</p>
  <div class="more">Read more</div>
</article>
<article class="abs card" style="left:754px">
  <div class="photo" role="img" aria-label="Pale chevron oak flooring sample" style="background:linear-gradient(135deg,#e4dccd,#cfc3ae)"></div>
  <h3>CHEVRON COLLECTION</h3>
  <p>Our timeless chevrons are produced to order. Available in the dimensions shown on page 7 and in our bespoke range of 28 finishes.</p>
  <div class="more">Read more</div>
</article>

<!-- process -->
<section class="abs process" role="img" aria-label="Dim interior with dark wood furniture and flooring behind the process steps">
  <h2 class="abs">FLOORING PROCESS</h2>
  <p class="abs lead">Our simple 4 step process allows you to create your own bespoke wood floor.</p>
  <p class="abs body">Now you've chosen your options our experienced colour technicians will create your wood floor here in the UK, so ensuring the highest British quality and prompt delivery. We also offer a bespoke colour matching service to create your perfect floor, so please feel free to provide us with a sample you would like us to match.</p>
  <div class="abs step" style="left:608px;top:112px">
    <svg width="40" height="40" viewBox="0 0 40 40"><rect x="4" y="8" width="28" height="28" fill="none" stroke="#c9a96a" stroke-width="2"/><path d="M14 28l18-18 4 4-18 18h-4z" fill="none" stroke="#c9a96a" stroke-width="2"/></svg>
    Choose your design
  </div>
  <div class="abs step" style="left:830px;top:112px">
    <svg width="40" height="40" viewBox="0 0 40 40"><rect x="4" y="6" width="32" height="28" fill="none" stroke="#c9a96a" stroke-width="2"/><path d="M4 14h32M10 20v8M16 20v5M22 20v8M28 20v5" stroke="#c9a96a" stroke-width="2"/></svg>
    Choose your dimensions
  </div>
  <div class="abs step" style="left:608px;top:236px">
    <svg width="40" height="40" viewBox="0 0 40 40"><rect x="4" y="10" width="32" height="22" fill="none" stroke="#c9a96a" stroke-width="2"/><path d="M4 10l16 13 16-13" fill="none" stroke="#c9a96a" stroke-width="2"/></svg>
    Choose your grade
  </div>
  <div class="abs finish">
    <h4>CHOOSE YOUR FINISHES</h4>
    <p>We use UV cured hardwax oil as our final protective layer. Available in Extra Matt, Matt, Satin &amp; Gloss finishes.</p>
  </div>
</section>

<!-- projects -->
<h2 class="abs sec-head" style="top:2122px"><span class="rule"></span><span>Previous <em>Projects</em></span><span class="rule"></span></h2>
<div class="img project-photo" style="left:170px;top:2211px" role="img" aria-label="Living room with warm honey oak plank floor and grey chair" ><div style="width:100%;height:100%;background:linear-gradient(180deg,#d9d6cf 0%,#c9a46c 55%,#b98a52 100%)"></div></div>
<article class="abs project" style="left:607px;top:2270px;width:420px">
  <h3>Brackenfold Smoked Oak</h3>
  <span class="tag">Lorem ipsul amet #215</span>
  <p>At vero eos et accusamus et iusto odio dignissimos ducimus qui blanditiis praesentium voluptatum deleniti atque corrupti quos dolores et quas molestias excepturi sint occaecati cupiditate.</p>
  <div class="link">View Details</div>
</article>
<article class="abs project" style="left:170px;top:2548px;width:418px;text-align:right">
  <h3>Thornmere Nordic Oak</h3>
  <span class="tag">Lorem ipsul amet #215</span>
  <p>At vero eos et accusamus et iusto odio dignissimos ducimus qui blanditiis praesentium voluptatum deleniti atque corrupti quos dolores et quas molestias excepturi sint occaecati cupiditate.</p>
  <div class="link">View Details</div>
</article>
<div class="img project-photo" style="left:610px;top:2484px" role="img" aria-label="Modern lounge with pale grey nordic oak floor and grey sofa"><div style="width:100%;height:100%;background:linear-gradient(180deg,#cfd0cd 0%,#b8b4ac 55%,#9e978c 100%)"></div></div>
<div class="abs btn btn-gold proj-btn">View Our All Products</div>

<!-- footer -->
<footer class="abs footer" role="img" aria-label="Dark wood floor interior behind the footer">
  <div class="abs brand" style="left:170px;top:50px"><span class="mark"></span><span class="name">PELLWICKHAUS</span></div>
  <p class="abs footer-about">With endless options available, you can choose the design, dimensions, grade, texture, colour and finish all produced to order in the UK.<span class="more">Read More</span></p>
  <div class="abs fcol" style="left:465px;top:66px">
    <h4>Services</h4>
    <ul><li><i class="tri"></i>Designs &amp; Dimensions</li><li><i class="tri"></i>Grading</li><li><i class="tri"></i>Textures &amp; Treatments</li><li><i class="tri"></i>Collections</li><li><i class="tri"></i>Shipping &amp; Returns</li><li><i class="tri"></i>Our Process</li><li><i class="tri"></i>Previous Work</li></ul>
  </div>
  <div class="abs fcol" style="left:640px;top:66px">
    <h4>Site Map</h4>
    <ul><li><i class="tri"></i>Home</li><li><i class="tri"></i>About</li><li><i class="tri"></i>Products</li><li><i class="tri"></i>Work Gallery</li><li><i class="tri"></i>Contact</li></ul>
  </div>
  <div class="abs fcol" style="left:755px;top:66px;width:280px">
    <h4>Connect With Us</h4>
    <ul>
      <li style="align-items:flex-start"><svg width="10" height="14" viewBox="0 0 10 14"><path d="M5 0a5 5 0 0 1 5 5c0 4-5 9-5 9S0 9 0 5a5 5 0 0 1 5-5z" fill="#fff"/><circle cx="5" cy="5" r="2" fill="#2b1e15"/></svg><span>Pellwickhaus LTD, 14 Harlow Lane, Fernbridge<br>NW7 4QT</span></li>
      <li><svg width="11" height="11" viewBox="0 0 12 12"><path d="M2 1h3l1 3-2 1a7 7 0 0 0 3 3l1-2 3 1v3c-6 1-10-3-9-9z" fill="#fff"/></svg>+44 (0)20 7946 0588</li>
      <li><svg width="12" height="9" viewBox="0 0 12 9"><rect x=".5" y=".5" width="11" height="8" fill="none" stroke="#fff"/><path d="M.5.5 6 5l5.5-4.5" fill="none" stroke="#fff"/></svg>enquiries@pellwickhaus.co.uk</li>
    </ul>
    <div style="display:flex;gap:12px;margin:14px 0 0 30px"><i class="dot"></i><i class="dot"></i><i class="dot"></i></div>
  </div>
</footer>
<div class="abs copyright">© Copyright 2019, Pellwickhaus LTD</div>

</body>
</html>
```